Signatur-Banner für 30 jähriges Jubiläum der Brambleton Device Works
Zielgruppe
Topic des Webbanner ist das 30-jährige Bestehen der Brambleton Device Works
Seit 1991 sind wir auf dem Markt.
Der/das Banner darf emotional sein, Gefühle ansprechen und wecken.
In diesem Kontext benötigen wir dann noch eine Version als Signatur-Banner.
Aktuell relevante Themen sind Embedded KI.
Wir arbeiten auf unserer Startseite bereits mit Webbannern.
Das Format darf identisch sein. Es wird über Slider Revolution eingebunden.
Weitere Informationen zum Unternehmen unter
www.bdw-k.de
Zielgruppe siehe Anhang.
Aufgabenstellung
Modernes Design, emotional, schlicht.
30 jähriges Jubiläum

```html
<!DOCTYPE html>
<html lang="de">
<head>
<meta charset="utf-8">
<title>Home - BDW-K.de</title>
<link href="https://fonts.googleapis.com/css2?family=Ubuntu:wght@400;500;700&family=Open+Sans:wght@700;800&family=Bungee&display=swap" rel="stylesheet">
<style>
  :root {
    --navy: #0b3a70;
    --pink: #e2127a;
    --grey-bar: #7a7b7a;
    --card: #f4f4f4;
    --text: #3a3a3a;
    --white: #ffffff;
  }
  * { margin: 0; padding: 0; box-sizing: border-box; }
  html, body { width: 1200px; height: 621px; overflow: hidden; background: var(--white); }
  body { position: relative; font-family: "Ubuntu", sans-serif; color: var(--text); }

  .top-bar { position: absolute; left: 0; top: 0; width: 1200px; height: 30px; background: var(--grey-bar); }
  .top-links { position: absolute; right: 174px; top: 0; line-height: 30px; font-size: 10.5px; color: var(--white); }
  .top-links span { margin-left: 10px; }

  .header { position: absolute; left: 0; top: 30px; width: 1200px; height: 58px; }
  .brand { position: absolute; left: 179px; top: 11px; color: var(--pink); font-family: "Ubuntu", sans-serif; font-weight: 700; font-size: 15px; line-height: 18px; }
  .brand small { display: block; font-size: 8px; line-height: 12px; padding-left: 50px; }
  .search { position: absolute; left: 425px; top: 13px; width: 273px; height: 26px; border: 1px solid #c9c9c9; font-size: 10px; color: #999; padding-left: 10px; line-height: 24px; }
  .search svg { position: absolute; right: 8px; top: 7px; }
  .contact-btn { position: absolute; left: 855px; top: 13px; width: 171px; height: 26px; background: var(--navy); color: var(--white); font-weight: 700; font-size: 10.5px; text-align: center; line-height: 26px; }

  .main-nav { position: absolute; left: 0; top: 88px; width: 1200px; height: 32px; background: var(--navy); }
  .nav-item { position: absolute; top: 0; height: 32px; line-height: 32px; color: var(--white); font-family: "Open Sans", sans-serif; font-weight: 800; font-size: 10px; letter-spacing: -0.1px; }
  .nav-item::after { content: ""; display: inline-block; margin-left: 3px; vertical-align: middle; border-left: 3px solid transparent; border-right: 3px solid transparent; border-top: 3px solid var(--white); }
  .nav-item.active { left: 166px; width: 87px; background: var(--pink); text-align: center; }

  .hero { position: absolute; left: 0; top: 120px; width: 1200px; height: 355px;
    background: linear-gradient(90deg, #d3157f 0%, #a41a78 22%, #4a2064 45%, #2a2c6e 60%, #1f5d9e 82%, #3aa2d8 100%); }
  .hero-title { position: absolute; left: 78px; top: 28px; color: var(--white); font-family: "Bungee", sans-serif; line-height: 1; }
  .hero-title .num { font-size: 70px; }
  .hero-title sup { font-size: 30px; vertical-align: top; position: relative; top: -4px; }
  .hero-title .word { display: block; font-size: 25px; margin-top: 6px; letter-spacing: 0.5px; }
  .hero-btn { position: absolute; left: 513px; top: 278px; width: 174px; height: 31px; border: 1px solid rgba(255,255,255,0.35); color: var(--white); font-weight: 700; font-size: 9.5px; letter-spacing: 1.6px; text-align: center; line-height: 29px; }

  .card { position: absolute; top: 475px; width: 268px; height: 146px; background: var(--card); padding: 18px 7px 0; overflow: hidden; }
  .card h2 { font-weight: 400; font-size: 18px; color: var(--navy); margin-bottom: 5px; }
  .card p { font-size: 10.4px; line-height: 13.7px; }
  .c1 { left: 179px; } .c2 { left: 468px; } .c3 { left: 757px; }

  .advice-tab { position: absolute; left: 1178px; top: 407px; width: 22px; height: 214px; background: var(--pink); }
  .advice-tab .label { position: absolute; left: 0; top: 118px; width: 22px; color: var(--white); font-size: 15px; transform-origin: 0 0; transform: rotate(-90deg) translate(0, 2px); white-space: nowrap; }
  .advice-tab .rule { position: absolute; left: 6px; top: 121px; width: 10px; height: 1px; background: var(--white); }
  .advice-tab .sq { position: absolute; left: 5px; width: 12px; height: 12px; background: var(--white); border-radius: 2px; }
</style>
</head>
<body>
  <div class="top-bar"><div class="top-links"><span>Willkommen bei BDW-K.de</span><span>News &amp; Events</span></div></div>

  <header class="header">
    <div class="brand">Brambleton Device Works<small>(Deutschland) GmbH</small></div>
    <div class="search">Hier den ganzen Katalog durchsuchen …
      <svg width="9" height="9" viewBox="0 0 10 10"><circle cx="4" cy="4" r="3" fill="none" stroke="#888" stroke-width="1.2"/><line x1="6.2" y1="6.2" x2="9" y2="9" stroke="#888" stroke-width="1.2"/></svg>
    </div>
    <div class="contact-btn">Kontakt</div>
  </header>

  <nav class="main-nav">
    <div class="nav-item active">⌂ BDW-K.DE</div>
    <div class="nav-item" style="left:270px">PANEL PCS / DISPLAYS</div>
    <div class="nav-item" style="left:411px">IPC-SYSTEME</div>
    <div class="nav-item" style="left:508px">IPC BOARDS</div>
    <div class="nav-item" style="left:602px">KOMMUNIKATION</div>
    <div class="nav-item" style="left:725px">MOBILE SYSTEME</div>
    <div class="nav-item" style="left:845px">⚙ SUPPORT</div>
    <div class="nav-item" style="left:939px">AKTUELLES</div>
  </nav>

  <section class="hero" role="img" aria-label="Zwei humanoide Roboter in einem pink-blau beleuchteten Raum, einer reicht dem anderen einen Cupcake mit Kerze">
    <div class="hero-title"><span class="num">30</span><sup>TH</sup><span class="word">anniversary</span></div>
    <div class="hero-btn">Weitere Informationen</div>
  </section>

  <article class="card c1">
    <h2>Lösungen</h2>
    <p>Sie suchen eine bewährte Standardlösung oder ein individuell entwickeltes Gesamtsystem?<br>Unsere erfahrenen Ingenieure finden für Sie die optimale Lösung: Industrie PCs, Embedded Systeme, Embedded Boards, Panel PCs sowie Individualsysteme für Ihre Industrieanwendung oder komplexe Anwendungen in</p>
  </article>
  <article class="card c2">
    <h2>Serviceleistungen</h2>
    <p>Sie verlassen sich bei Brambleton Device Works (Deutschland) GmbH neben hochwertigen Produkten auch auf eine erstklassige Dienstleistung. Seit 1991 sorgen persönliche und fachkundige Beratung durch unsere Ingenieure, kurzer Time-to-Market bei Entwicklungen, engagierte Betreuung und zuverlässige</p>
  </article>
  <article class="card c3">
    <h2>Branchen</h2>
    <p>Sie suchen eine System- oder Einzellösung für Ihre ganz besondere Aufgabenstellung? Dabei können Sie auf die Expertise unserer fachkundigen Ingenieure vertrauen. Für unterschiedliche Branchen gibt es Ansprechpartner, die im Thema sind. Sprechen Sie uns an.</p>
  </article>

  <aside class="advice-tab">
    <span class="label">Beratung</span>
    <span class="rule"></span>
    <span class="sq" style="top:140px"></span>
    <span class="sq" style="top:167px"></span>
    <span class="sq" style="top:194px"></span>
  </aside>
</body>
</html>
```